Trifold flyer for our dental clinic (the Bright Harbor Clinic)

The goal of this project is to design a trifold flyer for our dental clinic (the Bright Harbor Clinic). The winning design is expected to be creative, artistic and coherent with our logo.
Updates

Designs look the same

Target Market(s)

Young generation with dental need.

Industry/Entity Type

Dental Clinic

Font styles to use
Sans Serif

Colors
0355a3
85acd3
85cae6
0592cd
00a990
86cfc6
cedeed
cee9f5
cfeae6

Requirements
Must have
• See the attached sketch for content arrangement.

```html
<!DOCTYPE html>
<html lang="en">
<head>
<meta charset="utf-8">
<title>Bright Harbor Clinic – Trifold Flyer</title>
<link href="https://fonts.googleapis.com/css2?family=Lato:ital,wght@0,400;0,700;0,900;1,400;1,700&display=swap" rel="stylesheet">
<style>
  :root{
    --blue:#0592cd;
    --deep:#0355a3;
    --sky:#85cae6;
    --mist:#85acd3;
    --pale:#cee9f5;
    --pale2:#cedeed;
    --ink:#333a40;
    --grey:#6b7177;
    --paper:#ffffff;
    --stage:#e9ecef;
  }
  *{box-sizing:border-box;margin:0;padding:0}
  html,body{width:902px;height:1200px;overflow:hidden}
  body{background:var(--stage);font-family:"Lato",Arial,sans-serif;color:var(--ink);position:relative}
  .spread{position:absolute;left:83px;width:735px;height:571px;background:var(--paper);box-shadow:0 4px 14px rgba(0,0,0,.25)}
  .spread--outside{top:19px}
  .spread--inside{top:610px}
  .panel{position:absolute;top:0;width:245px;height:571px;overflow:hidden}
  .panel--1{left:0}.panel--2{left:245px}.panel--3{left:490px}
  .abs{position:absolute}
  svg.shape{position:absolute;left:0;top:0}
  .photo{position:absolute}
  .center{text-align:center;left:0;right:0}

  /* Meet us */
  .heading{color:var(--blue);font-weight:700;font-size:13px;letter-spacing:.3px}
  .doc-photo{position:absolute;left:14px;width:64px;height:64px;border-radius:50%;border:3px solid var(--blue);background:radial-gradient(circle at 50% 40%,#c9a58c,#5b4a44 70%,#2d2a2c)}
  .doc-name{position:absolute;left:92px;color:var(--blue);font-weight:700;font-size:8.5px}
  .doc-role{position:absolute;left:92px;color:var(--grey);font-size:8.5px;line-height:1.25}
  .bio{position:absolute;left:14px;right:12px;font-size:5.6px;line-height:1.45;text-align:justify;color:#555}
  .bio p+p{margin-top:4px}

  /* Reviews */
  .review{position:absolute;left:18px;right:14px;font-size:6.8px;line-height:1.38;font-style:italic;color:#444}
  .reviewer{display:block;margin-top:3px;font-style:normal;font-weight:700;color:var(--blue);font-size:6.3px;line-height:1.3}
  .badge-circle{position:absolute;left:86px;top:482px;width:72px;height:72px;border-radius:50%;background:#fff;border:3px solid var(--pale);display:flex;align-items:center;justify-content:center;text-align:center;color:var(--blue);font-size:7.5px;font-weight:700;line-height:1.2;padding:6px}

  /* Front */
  .brand{position:absolute;left:16px;top:30px;display:flex;align-items:center;gap:9px}
  .brand-mark{width:34px;height:34px;background:var(--blue);border-radius:3px}
  .brand-name{color:var(--blue);font-weight:700;font-size:17px;line-height:1.05}
  .call-label{color:#fff;font-weight:700;font-size:11.5px}
  .call-number{color:#fff;font-weight:700;font-size:22px}
  .pill{position:absolute;height:26px;border-radius:13px;display:flex;align-items:center;justify-content:center;font-weight:700}
  .pill--blue{background:linear-gradient(#4cc3ef,var(--blue));color:var(--deep);font-size:13px;box-shadow:0 2px 3px rgba(0,0,0,.3)}
  .pill--grey{background:linear-gradient(#fff,#c9cdd1);color:#333;font-size:11px;box-shadow:0 2px 3px rgba(0,0,0,.3)}
  .offers{color:var(--blue);font-weight:700;font-size:11.5px;line-height:1.35}

  /* Inside left */
  .promo{position:absolute;left:22px;color:#fff;font-weight:700;font-size:9.5px;line-height:1.3}
  .promo ul{list-style:none;margin-top:4px;font-weight:400;font-style:italic;font-size:8px}
  .promo li::before{content:"";display:inline-block;width:5px;height:5px;border-radius:50%;background:#fff;margin-right:8px}
  .tag{position:absolute;left:183px;width:40px;background:#fff;border-radius:3px;color:#333;text-align:center;font-size:6.5px;font-style:italic;padding:3px 0;line-height:1.2}
  .tag b{display:block;font-style:normal;font-size:10px}
  .services{position:absolute;list-style:none;color:var(--deep);font-style:italic;font-weight:700;font-size:9px;line-height:2.4}
  .services li::before{content:"";display:inline-block;width:6px;height:6px;border-radius:50%;background:var(--blue);margin-right:10px}

  /* Inside middle */
  .pay{color:var(--blue);font-weight:700;font-size:10.5px;line-height:1.25}
  .pay-strong{color:#222;font-weight:700;font-size:13px;line-height:1.2}
  .plan-circle{position:absolute;left:84px;top:200px;width:78px;height:78px;border-radius:50%;background:#fff;border:4px solid var(--pale);display:flex;align-items:center;justify-content:center;text-align:center;color:var(--blue);font-weight:700;font-size:10.5px;line-height:1.2}
  .svc-label{position:absolute;color:#222;font-size:6px;font-style:italic;line-height:1.4}
  .svc-label b{font-style:normal;font-size:7px;display:block}
  .save{position:absolute;width:36px;background:var(--blue);color:#fff;font-size:6.5px;text-align:center;line-height:1.25;padding:3px 0 5px;clip-path:polygon(0 0,100% 0,100% 100%,50% 88%,0 100%)}
  .fees{color:#fff;font-weight:700;font-size:10px;line-height:1.35}

  /* Inside right */
  .hours-title{color:var(--blue);font-weight:700;font-size:14px;line-height:1.2}
  .hours-row{position:absolute;left:18px;right:18px;display:flex;font-size:7px;color:#222}
  .hours-row .dots{flex:1;border-bottom:1px dotted #666;margin:0 2px 2px}
  .appt{color:#111;font-weight:700;font-size:14.5px}
  .phone-big{color:var(--blue);font-weight:700;font-size:24px}
  .icon-dot{position:absolute;left:115px;width:16px;height:16px;border-radius:50%;background:var(--blue)}
  .address{color:#222;font-size:9px;line-height:1.35}
  .web{color:#222;font-weight:700;font-size:9px}
  .footer-brand{position:absolute;top:318px;left:0;right:0;display:flex;justify-content:center;align-items:center;gap:7px}
  .footer-brand .brand-mark{width:20px;height:20px}
  .footer-brand .brand-name{font-size:10px}
</style>
</head>
<body>

<!-- OUTSIDE SPREAD -->
<section class="spread spread--outside">

  <!-- Meet us -->
  <div class="panel panel--1">
    <div class="abs center heading" style="top:20px">MEET US</div>

    <div class="doc-photo" style="top:40px" role="img" aria-label="Portrait photo of Dr. Lena Morrow"></div>
    <div class="doc-name" style="top:60px">LENA MORROW, DMD, MS</div>
    <div class="doc-role" style="top:72px">Board Certified Orthodontist</div>
    <div class="bio" style="top:114px">
      <p>Dr. Lena Morrow graduated with honors from a leading school of dental medicine and completed her specialty training in orthodontics with a master's degree. She is board certified and teaches as an assistant clinical professor. Outside the office she enjoys travel, yoga and playing the piano.</p>
      <p>She is a member of several national orthodontic associations and has helped develop care programs for children born with cleft lip and palate.</p>
    </div>

    <div class="doc-photo" style="top:242px" role="img" aria-label="Portrait photo of Dr. Victor Hale"></div>
    <div class="doc-name" style="top:258px">VICTOR HALE, DMD</div>
    <div class="doc-role" style="top:270px">Board Certified Pediatric Dentist<br>Board Certified Orthodontist</div>
    <div class="bio" style="top:320px">
      <p>Dr. Victor Hale is board certified in both pediatric dentistry and orthodontics. He has chaired a university department of orthodontics and pediatric dentistry and directed its graduate program for many years, earning the title of distinguished teaching professor.</p>
    </div>

    <div class="doc-photo" style="top:428px" role="img" aria-label="Portrait photo of Dr. Nadia Farrow"></div>
    <div class="doc-name" style="top:448px">DR. NADIA FARROW, DMD</div>
    <div class="doc-role" style="top:460px">General Dentist</div>
    <div class="bio" style="top:500px">
      <p>Dr. Nadia Farrow earned her DMD and completed a residency in advanced general practice. She is an enthusiastic, caring dentist whose warm personality helps patients feel at ease. In her spare time she enjoys painting and time with her family.</p>
    </div>
  </div>

  <!-- Reviews -->
  <div class="panel panel--2">
    <div class="photo" style="left:0;top:0;width:245px;height:215px;background:linear-gradient(135deg,#4fb3e4,#8fd0ef 55%,#5ab9e6)" role="img" aria-label="Blue-tinted photo of a smiling woman holding a clear aligner"></div>
    <svg class="shape" width="245" height="571" viewBox="0 0 245 571" aria-hidden="true">
      <path d="M0 212 Q122 110 245 212 L245 571 L0 571 Z" fill="#fff"/>
      <path d="M0 505 Q122 560 245 490 L245 571 L0 571 Z" fill="var(--blue)"/>
    </svg>
    <div class="abs center heading" style="top:192px">REVIEWS</div>
    <div class="review" style="top:214px">The Bright Harbor Clinic transformed my smile and helped me feel more confident! Overall, I was so pleased by the professional setting and the kindness of the staff. I also really appreciated how Dr. Morrow talked me through the process from beginning to end and was willing to work with what I wanted for results. I would absolutely recommend The Bright Harbor Clinic to friends and family!
      <span class="reviewer">MAYA QUINLAN<br>10/08/2017</span></div>
    <div class="review" style="top:322px">Friendly staff, pleasant atmosphere, great on time, and a very engaged doctor. Highly recommended!
      <span class="reviewer">PRIYA DALTON<br>5/15/2018</span></div>
    <div class="review" style="top:372px">This place is the best dentist ever. I've had a lot of other dentist but none quite like this place! Shes so funny and she shakes it all the time (like a snapshot). We are always having a good time, laughing, joking, and just all around havin fun in this office! not to mention its so clean and state of the art. The dentists there were always helping and explaining the process and made me very comfortable.
      <span class="reviewer">OWEN BRICKER<br>7/14/2017</span></div>
    <div class="badge-circle">BRIGHT HARBOR CLINIC</div>
  </div>

  <!-- Front -->
  <div class="panel panel--3">
    <div class="brand"><span class="brand-mark"></span><span class="brand-name">BRIGHT HARBOR<br>CLINIC</span></div>
    <div class="photo" style="left:40px;top:150px;width:205px;height:290px;background:radial-gradient(ellipse at 60% 45%,#f3d9c8,#d9b29a 45%,#e9eef2 80%)" role="img" aria-label="Photo of a smiling young woman"></div>
    <svg class="shape" width="245" height="200" viewBox="0 0 245 200" aria-hidden="true">
      <path d="M0 98 L245 98 L245 140 Q150 200 0 168 Z" fill="var(--blue)"/>
    </svg>
    <div class="abs center call-label" style="top:106px">CALL US NOW</div>
    <div class="abs center call-number" style="top:120px">555-014-2270</div>
    <div class="pill pill--blue" style="left:33px;top:447px;width:180px">SPECISL OFFERS</div>
    <div class="abs center offers" style="top:483px">$69 NEW PATIENT SPECIAL<br>$99 IN-OFFICE TEETH WHITEING<br>25%-40% OFF ON CLEARFIT</div>
  </div>
</section>

<!-- INSIDE SPREAD -->
<section class="spread spread--inside">

  <!-- Promos & services -->
  <div class="panel panel--1">
    <svg class="shape" width="245" height="571" viewBox="0 0 245 571" aria-hidden="true">
      <path d="M0 0 L245 0 L245 200 Q110 200 0 265 Z" fill="var(--blue)"/>
      <path d="M0 265 Q110 210 245 215" fill="none" stroke="var(--pale)" stroke-width="5"/>
    </svg>
    <div class="pill pill--grey" style="left:53px;top:26px;width:120px;height:22px">OUR PROMOS</div>
    <div class="promo" style="top:68px">$69 NEW PATIENT SPECIAL
      <ul><li>Exam</li><li>Cleaning</li><li>Digital X-rays</li></ul></div>
    <div class="tag" style="top:70px">Regular prices :<b>$500</b></div>
    <div class="promo" style="top:140px">$99 IN-OFFICE TEETH<br>WHITEING</div>
    <div class="tag" style="top:133px">Regular prices :<b>$700</b></div>
    <div class="promo" style="top:188px">25%-40% OFF ON CLEARFIT</div>
    <div class="promo" style="top:205px;font-size:8.5px">PLUS FREE <span style="color:#13233a">CONSULATION</span></div>
    <div class="abs center heading" style="top:257px;font-size:12.5px">OUR SERVICES</div>
    <ul class="services" style="left:48px;top:280px">
      <li>Cleaning and prevention</li>
      <li style="margin-left:6px">Cosmetic dentistry</li>
      <li style="margin-left:12px">Removable dentures</li>
      <li style="margin-left:18px">Orthodontics</li>
      <li style="margin-left:12px">Pediatric dentistry</li>
    </ul>
    <div class="photo" style="left:0;top:410px;width:245px;height:161px;background:linear-gradient(180deg,#dfe6ea,#e9cdb5 55%,#c49a80)" role="img" aria-label="Photo of a smiling family of four"></div>
  </div>

  <!-- Payment & savings plan -->
  <div class="panel panel--2" style="background:var(--blue)">
    <svg class="shape" width="245" height="571" viewBox="0 0 245 571" aria-hidden="true">
      <path d="M16 0 L229 0 L229 140 Q229 160 200 160 Q122 150 46 160 Q16 160 16 140 Z" fill="#fff"/>
      <path d="M0 330 Q90 260 245 225 L245 470 Q122 460 0 470 Z" fill="#fff"/>
      <path d="M0 330 Q90 260 245 225" fill="none" stroke="var(--pale)" stroke-width="6"/>
    </svg>
    <div class="abs center pay" style="top:18px">PAYMENT OPTIONS<br>AVAILABLE !</div>
    <div class="abs center pay" style="top:52px">FINANCING OPTIONS<br>AVAILABLE !</div>
    <div class="abs center pay-strong" style="top:88px">MOST INSURANCES<br>ACCEPTED !</div>
    <div class="abs center" style="top:168px;color:#fff;font-weight:700;font-size:11px;line-height:1.25">NO INSURANCE ?<br>TRY ONE</div>
    <div class="plan-circle">DENTAL<br>SAVINGS<br>PLAN</div>

    <div class="svc-label" style="left:20px;top:296px"><b>Preventive</b><br>Exam<br>X-ray<br>Professional<br>Cleaning</div>
    <div class="save" style="left:66px;top:318px">80%-100%<br>Savings</div>
    <div class="svc-label" style="left:20px;top:378px"><b>Filling</b>Crowns<br><b style="display:inline">In-office<br>whitening</b></div>
    <div class="save" style="left:66px;top:378px">40%-80%<br>Savings</div>
    <div class="svc-label" style="left:128px;top:378px"><b>Advances<br>dentenes</b></div>
    <div class="save" style="left:180px;top:380px">25%<br>Savings</div>
    <div class="svc-label" style="left:120px;top:418px"><b>Braces<br>(Orthodontics)</b></div>
    <div class="save" style="left:180px;top:418px">65%<br>Savings</div>

    <div class="abs center fees" style="top:496px">Annual Fees : $138<br>First coming member : 11.5/month<br>Lorem Ipsum is simply dummy<br>text : 72/month</div>
  </div>

  <!-- Hours & contact -->
  <div class="panel panel--3">
    <div class="photo" style="left:0;top:0;width:245px;height:45px;background:linear-gradient(180deg,#eef2f5,#fff)" role="img" aria-label="Faint photo of a smile and a dental mirror"></div>
    <div class="abs center hours-title" style="top:52px">CONVENIENT<br>SATURDAY HOURS!</div>
    <div class="hours-row" style="top:100px"><span>Tuesday &amp; Thursday</span><span class="dots"></span><span>9:30 am -5:00 pm</span></div>
    <div class="hours-row" style="top:116px"><span>Friday &amp; Saturday</span><span class="dots"></span><span>9:00 am -5:00 pm</span></div>
    <div class="abs center appt" style="top:138px">Call for an appointment!</div>
    <div class="abs center phone-big" style="top:157px">555-014-2270</div>
    <div class="icon-dot" style="top:196px">
      <svg width="16" height="16" viewBox="0 0 16 16" aria-hidden="true"><path d="M8 3.5a3 3 0 0 0-3 3c0 2.3 3 6 3 6s3-3.7 3-6a3 3 0 0 0-3-3zm0 4.2a1.2 1.2 0 1 1 0-2.4 1.2 1.2 0 0 1 0 2.4z" fill="#fff"/></svg>
    </div>
    <div class="abs center address" style="top:216px">275 Linden Avenue<br>Suite 401<br>Marlow, MA 02190</div>
    <div class="icon-dot" style="top:262px">
      <svg width="16" height="16" viewBox="0 0 16 16" aria-hidden="true"><g fill="none" stroke="#fff" stroke-width="1"><circle cx="8" cy="8" r="4.5"/><ellipse cx="8" cy="8" rx="2" ry="4.5"/><path d="M3.5 8h9"/></g></svg>
    </div>
    <div class="abs center web" style="top:283px">www.brightharborclinic.com</div>
    <div class="footer-brand"><span class="brand-mark"></span><span class="brand-name">BRIGHT HARBOR<br>CLINIC</span></div>
    <div class="photo" style="left:0;top:400px;width:245px;height:171px;background:linear-gradient(160deg,#eef0f1,#e3e6e8 60%,#d9ead9)" role="img" aria-label="Street map showing the clinic location"></div>
    <svg class="shape" width="245" height="571" viewBox="0 0 245 571" aria-hidden="true">
      <path d="M0 395 Q140 390 245 350 L245 400 L0 400 Z" fill="#fff"/>
      <path d="M0 405 Q140 398 245 352 L245 380 Q140 418 0 418 Z" fill="var(--blue)"/>
    </svg>
  </div>
</section>

</body>
</html>
```